Corvena Brand Nacho Sliced Jalapeños

Company Background Information:
Corvena Brand Farms is a family owned and operated business since 1981. Our Jalapeños are grown through sustainable practices environmentally socially and economically. We are a company based in Mexico looking to enter the U.S. and international retail market.
Packaging Design Description:
We manufacture Nacho Sliced Jalapeño Peppers on a stand up pouch bag with a zipper. We currently are labeling as can be seen in attached picture, but I am looking for a design to be printed in the bag on both sides front and back that will stand out in the shelf of the retail market.
Attached are the photo files of the bag dimensions and the finished product with current label.
Requirements:
1. Logo: Corvena Brand (Attached in file)
2. Name of Product: Nacho Sliced Jalapeño Peppers
3. Generic Nutrition Facts panel.
4. " Best Before: " (For expiration date purposes)
5. " Refrigerate after opening"
6. Ingredients: Jalapeño Peppers, Water, Vinegar, Salt, Oregano, Bay Leaf, Garlic, Thyme & Calcium Chloride
7. Net Wt. 16 oz
8. Generic Bar Code
9. Processed by: Empacadora Riscos del Tamar S.A. de C.V.
Av. Quiroba 274 Int. 8 Col. Centro
Guaymas, Son. Mexico
10. www.corvenabrand.example
11. e-mail info@corvenabrand.example
12. Phone: 52(987)314-2068
We would like a fresh appearance. Somewhat traditional. It is also directed towards a more economical market.
Target Market(s)
Our target market is mostly the latino population in the United States, the growing diversity of cultures in the US is helping people try different cuisines, spicy foods in our case.
Industry/Entity Type
Business
Look and feel

```html
<!DOCTYPE html>
<html lang="en">
<head>
<meta charset="utf-8">
<title>Corvena Brand – Nacho Sliced Jalapeño Peppers pouch</title>
<link rel="stylesheet" href="https://fonts.googleapis.com/css2?family=Oswald:wght@300;400;500;600;700&family=Barlow+Condensed:wght@400;500;600&display=swap">
<style>
  :root{
    --bg:#e4e4e4;
    --yellow:#f8c51c;
    --amber:#f59b1e;
    --orange:#ea4f1f;
    --red:#c4161c;
    --ink-red:#7a1a12;
    --pale-yellow:#fde08a;
    --white:#ffffff;
    --label-ink:#222222;
    --pepper:#3d9a2a;
    --pepper-dark:#1f6214;
    --border-red:#b8171b;
    --border-gold:#f3a81c;
  }
  *{box-sizing:border-box;margin:0;padding:0}
  html,body{width:1200px;height:960px;overflow:hidden}
  body{background:var(--bg);font-family:"Oswald",sans-serif;position:relative}

  .pouch{
    position:absolute;top:110px;width:520px;height:740px;
    background:linear-gradient(180deg,var(--yellow) 0%,var(--amber) 30%,var(--orange) 52%,var(--red) 78%,var(--red) 100%);
    overflow:hidden;
  }
  .pouch--front{left:50px}
  .pouch--back{left:630px}

  .pouch__border{
    position:absolute;top:0;bottom:0;width:42px;
    background:repeating-linear-gradient(180deg,var(--border-red) 0 22px,var(--border-gold) 22px 44px);
  }
  .pouch__border--left{left:0}
  .pouch__border--right{right:0}

  .pouch__zipper{
    position:absolute;left:42px;right:42px;top:118px;height:2px;
    background:rgba(122,26,18,.35);
  }

  .tear-hint{
    position:absolute;top:62px;right:62px;
    font-weight:500;font-size:19px;letter-spacing:.5px;color:var(--ink-red);
    display:flex;align-items:center;gap:10px;
  }

  .brand{
    display:flex;align-items:center;gap:10px;
    font-family:"Oswald",sans-serif;font-weight:600;color:#2b1a10;
  }
  .brand__dot{border-radius:50%;background:var(--pepper)}
  .pouch--front .brand{position:absolute;top:190px;left:0;right:0;justify-content:center;font-size:58px}
  .pouch--front .brand__dot{width:26px;height:26px}

  .flames{
    position:absolute;left:42px;right:42px;top:250px;height:420px;
    background:radial-gradient(ellipse at 50% 70%,rgba(255,214,60,.55) 0%,rgba(255,140,30,.35) 40%,rgba(255,90,20,0) 70%);
  }

  .product-title{
    position:absolute;top:330px;left:0;right:0;text-align:center;
    font-weight:600;font-size:52px;line-height:1.1;color:var(--white);
    letter-spacing:.5px;text-shadow:0 2px 4px rgba(90,10,10,.45);
  }

  .peppers{
    position:absolute;left:95px;top:480px;width:360px;height:170px;
    border-radius:90px 90px 70px 70px;
    background:radial-gradient(ellipse at 40% 45%,#d9e9a6 0%,#8fcb50 22%,var(--pepper) 48%,var(--pepper-dark) 100%);
  }

  .net-weight{
    position:absolute;bottom:30px;left:0;right:0;text-align:center;
    color:var(--white);font-weight:500;line-height:1.1;
  }
  .net-weight span{display:block}
  .net-weight__label{font-size:22px}
  .net-weight__value{font-size:30px}

  /* back */
  .zip-hint{
    position:absolute;top:92px;left:56px;
    font-weight:500;font-size:16px;color:var(--ink-red);display:flex;align-items:center;gap:6px;
  }
  .back-header{position:absolute;top:150px;left:62px;right:62px;display:flex;align-items:center;gap:28px}
  .back-header .brand{font-size:34px}
  .back-header .brand__dot{width:16px;height:16px}
  .back-title{font-weight:600;font-size:21px;line-height:1.15;color:var(--ink-red)}

  .ingredients{
    position:absolute;top:240px;left:62px;right:62px;
    font-family:"Barlow Condensed",sans-serif;font-weight:500;font-size:14.5px;line-height:1.6;color:var(--pale-yellow);
  }
  .storage-note{
    position:absolute;top:300px;left:62px;right:62px;
    font-weight:300;font-size:22px;color:var(--white);letter-spacing:.5px;
    padding-bottom:8px;border-bottom:1px solid rgba(255,255,255,.8);
  }

  .nutrition{
    position:absolute;top:362px;left:62px;width:110px;
    background:var(--white);border:1px solid #222;padding:4px 5px;
    font-family:"Barlow Condensed",sans-serif;color:#111;font-size:8.5px;
  }
  .nutrition__title{font-family:"Oswald",sans-serif;font-weight:700;font-size:11px;border-bottom:1px solid #111}
  .nutrition__serving{text-align:center;line-height:1.2;padding:2px 0;border-bottom:2px solid #111}
  .nutrition table{width:100%;border-collapse:collapse}
  .nutrition td{border-bottom:1px solid #999;padding:1px 0;line-height:1.15}
  .nutrition td:last-child{text-align:right}
  .nutrition .indent{padding-left:10px}
  .nutrition .head td{text-align:right;font-size:7.5px}

  .processor{
    position:absolute;top:364px;left:190px;right:62px;
    font-family:"Barlow Condensed",sans-serif;font-size:11.5px;line-height:1.3;color:var(--pale-yellow);
  }
  .back-net{
    position:absolute;top:478px;left:190px;font-weight:500;font-size:16px;color:var(--white);
  }
  .back-divider{position:absolute;top:530px;left:62px;right:62px;height:1px;background:rgba(255,255,255,.8)}

  .lot-box{
    position:absolute;top:560px;left:62px;width:140px;height:60px;background:var(--white);
    font-family:"Barlow Condensed",sans-serif;font-size:11px;color:var(--label-ink);padding:6px 8px;line-height:1.6;
  }
  .barcode{
    position:absolute;top:560px;left:222px;right:62px;height:60px;background:var(--white);
    display:flex;align-items:flex-end;justify-content:center;padding-bottom:5px;
    font-family:"Barlow Condensed",sans-serif;font-size:13px;letter-spacing:2px;color:var(--label-ink);
  }
  .marks{position:absolute;top:636px;left:66px;display:flex;gap:14px}
  .mark{width:16px;height:16px;border-radius:50%;border:1.5px solid var(--white)}
</style>
</head>
<body>

<section class="pouch pouch--front" aria-label="Front of pouch">
  <div class="pouch__border pouch__border--left" role="img" aria-label="Traditional woven diamond pattern band"></div>
  <div class="pouch__border pouch__border--right" role="img" aria-label="Traditional woven diamond pattern band"></div>
  <div class="pouch__zipper"></div>

  <p class="tear-hint">TEAR HERE TO OPEN
    <svg width="9" height="12" viewBox="0 0 9 12"><path d="M0 0L9 6L0 12Z" fill="#7a1a12"/></svg>
  </p>

  <div class="flames" role="img" aria-label="Fire flames illustration"></div>

  <div class="brand"><span class="brand__dot"></span>Corvena</div>

  <h1 class="product-title">NACHO SLICED<br>JALAPEÑO PEPPERS</h1>

  <div class="peppers" role="img" aria-label="Photo of sliced green jalapeño peppers"></div>

  <p class="net-weight"><span class="net-weight__label">NET WT.</span><span class="net-weight__value">16 OZ</span></p>
</section>

<section class="pouch pouch--back" aria-label="Back of pouch">
  <div class="pouch__border pouch__border--left" role="img" aria-label="Traditional woven diamond pattern band"></div>
  <div class="pouch__border pouch__border--right" role="img" aria-label="Traditional woven diamond pattern band"></div>
  <div class="pouch__zipper"></div>

  <p class="zip-hint">
    <svg width="14" height="12" viewBox="0 0 14 12"><path d="M12 11C12 5 8 3 3 4" stroke="#7a1a12" stroke-width="2" fill="none"/><path d="M0 4L5 0L5 8Z" fill="#7a1a12"/></svg>
    OPEN-CLOSE ZIPLOCK TO KEEP'EM FRESH!
  </p>

  <div class="back-header">
    <div class="brand"><span class="brand__dot"></span>Corvena</div>
    <h2 class="back-title">NACHO SLICED<br>JALAPEÑO PEPPERS</h2>
  </div>

  <p class="ingredients">Ingredients: Jalapeño Peppers, Water, Vinegar, Salt, Oregano, Bay Leaf, Garlic, Thyme &amp; Calcium Chloride</p>

  <p class="storage-note">REFRIGERATE AFTER OPENING</p>

  <div class="nutrition">
    <div class="nutrition__title">NUTRITION FACTS</div>
    <div class="nutrition__serving">Servings per package: ?<br>Serving size: ?</div>
    <table>
      <tr class="head"><td colspan="2">Amount / 100ml</td></tr>
      <tr><td>Energy</td><td>40 Kcal</td></tr>
      <tr><td>Carbohydrates</td><td>10.0 g</td></tr>
      <tr><td class="indent">Sugar</td><td>9.5 g</td></tr>
      <tr><td>Protein</td><td>0 g</td></tr>
      <tr><td>Fats</td><td>0 g</td></tr>
      <tr><td>Sodium</td><td>30 mg</td></tr>
    </table>
  </div>

  <p class="processor">
    Processed by:<br>
    Empacadora Riscos del Tamar S.A. de C.V.<br>
    Av. Quiroba 274 Int. 8 Col. Centro<br>
    Guaymas, Son. Mexico<br>
    Phone: 52(987)314-2068<br>
    www.corvenabrand.example<br>
    e-mail info@corvenabrand.example
  </p>

  <p class="back-net">NET WT. 16 OZ</p>
  <div class="back-divider"></div>

  <div class="lot-box">LOT NR:<br>BEST BEFORE:</div>
  <div class="barcode" role="img" aria-label="Generic product barcode label">0 123456 789999</div>
  <div class="marks" role="img" aria-label="Certification and recycling marks">
    <span class="mark"></span><span class="mark"></span><span class="mark"></span><span class="mark"></span>
  </div>
</section>

</body>
</html>
```